Kereru Creative Food Fiesta

We are holding our inaugural event on the 21st October 2022 on the FieldSolve campus in Palmerston North., from 10am until 2pm.The event will be a mix of Fourth year Food Technology students presenting their student projects and local producers show casing and educating around their products. The event is bought to you by CropNest along with Tarrowby Vale District Council and RIVO. The overall plan is to bring a spotlight to the amount of research and food related businesses are on this side of the river. The event will be free to enter and there will be food and products to purchase, but the main focus is on education.

```html
<!DOCTYPE html>
<html lang="en">
<head>
<meta charset="utf-8">
<title>Kereru Creative Food Fiesta</title>
<link rel="stylesheet" href="https://fonts.googleapis.com/css2?family=Ultra&family=Oswald:wght@600;700&display=swap">
<style>
  :root {
    --sky-blue: #3a9af5;
    --festival-orange: #fb9a37;
    --festival-red: #f50e0e;
    --cream: #f7f3e6;
    --ink: #111111;
    --white: #ffffff;
    --footer: #0d0d0d;
  }
  * { margin: 0; padding: 0; box-sizing: border-box; }
  html, body { width: 741px; height: 1200px; overflow: hidden; background: var(--white); }
  .poster {
    position: relative;
    width: 741px;
    height: 1200px;
    overflow: hidden;
    background: var(--festival-orange);
    font-family: "Ultra", Georgia, serif;
  }
  .hero-art { position: absolute; left: 0; top: 0; width: 741px; height: 630px; }
  .pattern-column {
    position: absolute;
    left: 552px; top: 296px;
    width: 189px; height: 787px;
    background: linear-gradient(180deg, var(--cream) 0%, var(--festival-orange) 30%, var(--festival-red) 50%, var(--sky-blue) 65%, var(--festival-orange) 82%, var(--festival-red) 100%);
  }
  .title {
    position: absolute;
    left: 24px; top: 330px;
    width: 470px;
    color: var(--white);
    text-align: center;
    line-height: 1;
  }
  .title .line { display: block; font-size: 70px; letter-spacing: -1px; margin-bottom: 16px; }
  .title .line-condensed {
    font-family: "Oswald", "Arial Narrow", sans-serif;
    font-weight: 700;
    font-size: 92px;
    letter-spacing: -1px;
    margin-top: -6px;
  }
  .info-block { position: absolute; top: 654px; text-align: center; }
  .info-block.date { left: 0; width: 240px; }
  .info-block.venue { left: 280px; width: 240px; }
  .info-label { font-size: 22px; color: var(--ink); margin-bottom: 12px; }
  .info-text { font-size: 21px; color: var(--white); line-height: 1.4; }
  .info-block.venue .info-text {
    font-family: "Oswald", "Arial Narrow", sans-serif;
    font-weight: 600;
    font-size: 25px;
    line-height: 1.3;
  }
  .highlight {
    position: absolute;
    width: 170px; height: 170px;
    border-radius: 50%;
    background: var(--festival-red);
    color: var(--white);
    display: flex; flex-direction: column; align-items: center; justify-content: center;
    text-align: center;
    line-height: 1.6;
  }
  .highlight .big { font-size: 24px; }
  .highlight .small { font-size: 19px; letter-spacing: -0.5px; }
  .highlight.students { left: -3px; top: 808px; }
  .highlight.chef { left: 177px; top: 804px; }
  .highlight.truck { left: 353px; top: 798px; }
  .free-entry {
    position: absolute;
    left: 22px; top: 990px;
    font-family: "Oswald", "Arial Narrow", sans-serif;
    font-weight: 700;
    font-size: 38px;
    color: var(--white);
    transform: rotate(-32deg);
    transform-origin: left center;
  }
  .sponsor-intro {
    position: absolute;
    left: 196px; top: 1024px;
    font-size: 22px;
    color: var(--white);
  }
  .sponsors {
    position: absolute;
    left: 0; top: 1083px;
    width: 741px; height: 117px;
    background: var(--footer);
    display: flex; align-items: center; justify-content: space-around;
    padding: 0 16px;
    color: var(--white);
  }
  .sponsor { font-family: "Oswald", "Arial Narrow", sans-serif; font-weight: 600; text-align: center; }
  .sponsor.lead { font-size: 44px; }
  .sponsor.council { font-size: 22px; line-height: 1.1; width: 220px; }
  .sponsor.agency { font-size: 50px; letter-spacing: 2px; }
</style>
</head>
<body>
<main class="poster">
  <svg class="hero-art" viewBox="0 0 741 630" xmlns="http://www.w3.org/2000/svg">
    <defs>
      <linearGradient id="landscape" x1="0" y1="0" x2="0" y2="1">
        <stop offset="0" stop-color="#c9d8e8"/>
        <stop offset="0.45" stop-color="#a7bfd6"/>
        <stop offset="0.62" stop-color="#8aa25a"/>
        <stop offset="0.8" stop-color="#4d6a3a"/>
        <stop offset="1" stop-color="#3b4a55"/>
      </linearGradient>
    </defs>
    <rect class="sky-field" x="0" y="0" width="741" height="630" fill="var(--sky-blue)"/>
    <path class="landscape-photo" role="img" aria-label="Photo of green rolling hills with trees beside a calm lake under a cloudy sky"
          d="M0 0 H741 V275 C640 262 520 240 400 248 C260 256 130 190 0 150 Z" fill="url(#landscape)"/>
    <path class="band band-orange" d="M0 150 C130 190 260 256 400 248 C520 240 640 262 741 275 V292 C640 278 520 258 400 262 C260 270 120 205 0 168 Z" fill="var(--festival-orange)"/>
    <path class="band band-red" d="M0 190 C80 230 170 280 250 285 C330 290 380 265 450 270 C560 278 660 310 741 345 V328 C660 296 560 264 450 258 C380 254 330 276 250 272 C170 266 80 215 0 176 Z" fill="var(--festival-red)"/>
  </svg>

  <div class="pattern-column" role="img" aria-label="Decorative zigzag pattern of cream, orange, red and blue triangles"></div>

  <h1 class="title">
    <span class="line">Kereru</span>
    <span class="line">Creative</span>
    <span class="line line-condensed">Food Fiesta</span>
  </h1>

  <section class="info-block date">
    <h2 class="info-label">Date AND Time</h2>
    <p class="info-text">21st October 2022<br>10am until 2pm</p>
  </section>
  <section class="info-block venue">
    <h2 class="info-label">Venue</h2>
    <p class="info-text">FieldSolve Campus<br>in Palmerston North</p>
  </section>

  <div class="highlight students"><span class="big">Student</span><span class="small">presentation</span></div>
  <div class="highlight chef"><span class="big">Chef</span><span class="small">Demonstration</span></div>
  <div class="highlight truck"><span class="big">Food</span><span class="big">truck</span></div>

  <p class="free-entry">Free to Enter</p>
  <p class="sponsor-intro">Brought to you by</p>

  <footer class="sponsors">
    <span class="sponsor lead">CropNest</span>
    <span class="sponsor council">TARROWBY VALE DISTRICT COUNCIL</span>
    <span class="sponsor agency">RIVO</span>
  </footer>
</main>
</body>
</html>
```